Hello Creative Minds!
Our business is after a elegant and classy flyer that draws attention!
The business is Velmora Turf - Lawn Rejuvenation Services. We provide services that maintain a healthy and vibrant green lawn through the tough Australian seasons. The products we use limits the water needed to keep grass green to a minimum - practically none at all! This not only helps the home owner or home seller but the environment by limiting the use of water that is needed to create a green lawn. The products we use are made from natural ingredients that are and pet friendly.
This fly will be our introductory offer to the market. Below are the required points that need to be on the flyer. Attached is the business logo, before & after pictures and 1 example of the LAYOUT not DESIGN of what the flyer should be laid out like or similar to. Feel free to use different 'Lawn Mower' pictures.
All the best; if you need any questions answered please feel free to message.
REQUIRED POINTS (Please re-phrase were possible);
*Instantly restores the natural green colour of grass – year round
*Lasts for up to 3 months
*Substantially reduces watering needs
*Pet friendly
*Stays green during droughts and water restrictions
*UV fade resistant
*Won’t bleed, run, or stain once absorbed into the grass
*Safe for the environment, pets and people
*Works in extreme heat, cold and frost
*Organic and natural – no harmful chemicals
*Reduces the amount of fertilizer
and water used on lawns
*Kerb appeal is essential for getting your property sold for the highest price possible
SERVICES & PRICING
Lawn maintenance (cut & trim) starting from $60
Lawn rejuvenation starting from $80 (Only $27 a month for 3 months)*
Package deal starting from $120
Introductory offer: 25% off all services. Refer a friend, when they book you receive another 25% off your next service.
LOCATIONS
Nowra to Sydney
CONTACT NUMBER
Will be posted with the winner - please leave an area for this.
SOCIAL MEDIA
Please add Chatterloop and Snapvista logo's
Updates
Competition has finished, thank you to all that have participated! I will review and comment on the flyers that need assistance. All the best with future designs!
Target Market(s)
home owners, home sellers, property developers, real estates and nursing homes and government housing.
Industry/Entity Type
Lawn Care
Look and feel
Each slider illustrates characteristics of the customer's brand and the style your logo design should communicate.

```html
<!DOCTYPE html>
<html lang="en">
<head>
<meta charset="utf-8">
<title>Velmora Turf - Lawn Rejuvenation Services</title>
<link rel="stylesheet" href="https://fonts.googleapis.com/css2?family=Lato:ital,wght@0,400;0,700;0,900;1,400;1,700&display=swap">
<style>
  :root {
    --navy: #2a2e39;
    --lime: #8cc63f;
    --lime-bright: #9fd13f;
    --mint: #e2edd3;
    --green-deep: #178a1c;
    --ink: #23262e;
    --white: #ffffff;
    --stage: #dcdcdc;
  }
  * { box-sizing: border-box; margin: 0; padding: 0; }
  html, body { width: 1200px; height: 1200px; overflow: hidden; }
  body { background: var(--stage); font-family: "Lato", sans-serif; color: var(--ink); position: relative; }

  .flyer { position: absolute; left: 160px; top: 30px; width: 880px; height: 1140px; overflow: hidden; background: var(--mint); }
  .flyer-shapes { position: absolute; inset: 0; }

  .brand { position: absolute; left: 30px; top: 70px; width: 360px; text-align: center; color: var(--white); }
  .brand-name { font-size: 46px; font-weight: 700; letter-spacing: 1px; line-height: 1; }
  .brand-tag { margin-top: 10px; font-size: 11px; letter-spacing: 4.6px; font-weight: 400; }

  .intro { position: absolute; left: 28px; top: 417px; width: 400px; font-size: 16.6px; line-height: 20.7px; font-style: italic; font-weight: 700; color: var(--ink); }

  .price-row { position: absolute; left: 0; width: 417px; height: 42px; background: var(--white); border-radius: 0 22px 22px 0; }
  .price-row .label { position: absolute; left: 26px; top: 5px; font-size: 15.5px; font-weight: 900; line-height: 17px; color: var(--ink); }
  .price-row .label::before { content: ""; position: absolute; left: -12px; top: 6px; width: 5px; height: 5px; border-radius: 50%; background: var(--lime); }
  .price-row .sub { font-style: italic; font-weight: 400; font-size: 14.5px; }
  .price-row .note { font-size: 13px; font-weight: 700; }
  .price-tag { position: absolute; right: 3px; top: 3px; width: 92px; height: 36px; border-radius: 18px; background: var(--navy); color: var(--lime-bright); font-weight: 900; font-size: 24px; text-align: center; line-height: 36px; }
  .offer-row { height: 60px; }
  .offer-row .accent { color: var(--lime); }
  .offer-row .sub { display: block; font-size: 13.5px; line-height: 17px; margin-top: 2px; }

  .benefits { position: absolute; left: 464px; top: 0; width: 410px; list-style: none; }
  .benefit { position: absolute; left: 0; width: 400px; display: flex; align-items: center; transform: translateY(-50%); }
  .benefit-icon { flex: 0 0 42px; width: 42px; height: 42px; }
  .benefit-text { margin-left: 10px; font-size: 16.5px; line-height: 21px; color: var(--ink); }

  .highlights { position: absolute; left: 304px; top: 952px; list-style: none; color: var(--lime-bright); font-size: 16.5px; line-height: 21px; }
  .highlights li { padding-left: 12px; position: relative; }
  .highlights li::before { content: "•"; position: absolute; left: 0; }

  .contact { position: absolute; left: 318px; top: 1060px; width: 240px; text-align: center; color: var(--white); font-weight: 700; font-size: 19px; line-height: 26px; }

  .socials { position: absolute; left: 588px; top: 1073px; list-style: none; color: var(--white); font-size: 13px; font-weight: 700; }
  .socials li { display: flex; align-items: center; height: 24px; }
  .socials .dot { width: 16px; height: 16px; border-radius: 50%; background: var(--lime); border: 2px solid var(--navy); margin-right: 7px; }

  .locations { position: absolute; left: 715px; top: 972px; width: 138px; height: 138px; border-radius: 50%; background: var(--navy); border: 5px solid var(--white); text-align: center; color: var(--white); padding-top: 14px; }
  .locations-title { color: var(--lime-bright); font-weight: 700; font-size: 17px; margin-top: 2px; }
  .locations-area { font-style: italic; font-weight: 700; font-size: 15px; line-height: 19px; }

  .compare { position: absolute; left: 19px; top: 861px; width: 262px; height: 262px; border-radius: 50%; overflow: hidden; border: 5px solid var(--white); background: var(--white); }
  .compare-half { position: absolute; left: 0; width: 100%; height: 50%; }
  .compare-before { top: 0; background: linear-gradient(180deg, #5f6266 0%, #a9a57a 55%, #555a60 100%); }
  .compare-after { top: 50%; border-top: 3px solid var(--white); background: linear-gradient(180deg, #6d7074 0%, #5f9a3e 55%, #4f5359 100%); }
  .compare-label { position: absolute; left: 100px; color: var(--white); font-weight: 900; font-size: 15px; }
</style>
</head>
<body>
<main class="flyer">
  <svg class="flyer-shapes" width="880" height="1140" viewBox="0 0 880 1140" aria-hidden="true">
    <defs>
      <linearGradient id="lawn" x1="0" y1="0" x2="1" y2="1">
        <stop offset="0" stop-color="#6fb12c"/>
        <stop offset="0.6" stop-color="#58a126"/>
        <stop offset="1" stop-color="#3f7f1c"/>
      </linearGradient>
      <linearGradient id="footer-band" x1="0" y1="0" x2="1" y2="0">
        <stop offset="0" stop-color="#2a2e39"/>
        <stop offset="0.55" stop-color="#5a5e65"/>
        <stop offset="1" stop-color="#a7aaae"/>
      </linearGradient>
      <linearGradient id="footer-wave" x1="0" y1="0" x2="1" y2="0">
        <stop offset="0.2" stop-color="#2a2e39"/>
        <stop offset="0.6" stop-color="#1c6b22"/>
        <stop offset="1" stop-color="#178a1c"/>
      </linearGradient>
    </defs>
    <rect class="hero-photo" x="0" y="0" width="880" height="430" fill="url(#lawn)" role="img" aria-label="Photo of a push lawn mower on freshly cut green grass"/>
    <path class="hero-band" d="M880 245 V335 C760 392 600 412 430 408 C600 398 770 350 880 245 Z" fill="var(--navy)"/>
    <path class="hero-swoosh" d="M0 245 C120 350 300 410 470 406 C650 402 800 372 880 335 V352 C780 405 620 440 450 440 C260 440 90 385 0 312 Z" fill="var(--white)"/>
    <path class="panel-services" d="M0 312 C90 385 260 440 441 440 V940 H0 Z" fill="var(--lime)"/>
    <path class="panel-benefits" d="M441 440 C620 440 780 405 880 352 V940 H441 Z" fill="var(--mint)"/>
    <path class="header-cap" d="M0 0 H440 C420 120 310 222 160 215 C95 212 40 200 0 185 Z" fill="var(--navy)" stroke="var(--white)" stroke-width="4"/>
    <rect class="footer-band" x="0" y="938" width="880" height="202" fill="url(#footer-band)"/>
    <path class="footer-line" d="M0 1082 C220 1028 520 1018 880 1058" fill="none" stroke="var(--white)" stroke-width="5"/>
    <path class="footer-wave" d="M0 1085 C220 1031 520 1021 880 1061 V1140 H0 Z" fill="url(#footer-wave)"/>
  </svg>

  <header class="brand">
    <div class="brand-name">Velmora Turf</div>
    <div class="brand-tag">LAWN REJUVENATION SERVICES</div>
  </header>

  <p class="intro">We provide services that maintain a healthy &amp; vibrant green lawn through the tough Australian seasons. The products we use limits the water needed to keep grass green to a minimum - practically none at all! This not only helps the home owner or home seller but the environment by limiting the use of water that is needed to create a green lawn. The products we use are made from natural ingredients that are and pet friendly.</p>

  <section class="services">
    <div class="price-row" style="top:626px">
      <div class="label">LAWN MAINTENANCE (CUT &amp; TRIM)<br><span class="sub">starting from</span></div>
      <div class="price-tag">$60</div>
    </div>
    <div class="price-row" style="top:680px">
      <div class="label">LAWN REJUVENATION <span class="sub">starting from</span><br><span class="note">(Only $27 a month for 3 months)*</span></div>
      <div class="price-tag">$80</div>
    </div>
    <div class="price-row" style="top:735px">
      <div class="label">PACKAGE DEAL<br><span class="sub">starting from</span></div>
      <div class="price-tag">$120</div>
    </div>
    <div class="price-row offer-row" style="top:787px">
      <div class="label">INTRODUCTORY OFFER <span class="accent">25% OF ALL SERVICES</span><span class="sub">Refer a friend, when they book you receive another 25% off your next service.</span></div>
    </div>
  </section>

  <ul class="benefits">
    <li class="benefit" style="top:445px"><svg class="benefit-icon" viewBox="0 0 42 42"><circle cx="21" cy="21" r="20" fill="var(--lime)" stroke="var(--white)" stroke-width="2"/><path d="M21 10 C16 17 14 20 14 24 a7 7 0 0 0 14 0 C28 20 26 17 21 10 Z" fill="var(--navy)"/></svg><span class="benefit-text">Substantially reduces watering needs</span></li>
    <li class="benefit" style="top:487px"><svg class="benefit-icon" viewBox="0 0 42 42"><circle cx="21" cy="21" r="20" fill="var(--lime)" stroke="var(--white)" stroke-width="2"/><circle cx="21" cy="25" r="6" fill="var(--navy)"/><circle cx="13" cy="18" r="3" fill="var(--navy)"/><circle cx="18" cy="13" r="3" fill="var(--navy)"/><circle cx="24" cy="13" r="3" fill="var(--navy)"/><circle cx="29" cy="18" r="3" fill="var(--navy)"/></svg><span class="benefit-text">Pet friendly</span></li>
    <li class="benefit" style="top:539px"><svg class="benefit-icon" viewBox="0 0 42 42"><circle cx="21" cy="21" r="20" fill="var(--lime)" stroke="var(--white)" stroke-width="2"/><circle cx="21" cy="21" r="11" fill="var(--navy)"/><path d="M16 21 l4 4 l7 -8" fill="none" stroke="var(--lime)" stroke-width="2.5"/></svg><span class="benefit-text">Stays green during droughts &amp;<br>water restrictions</span></li>
    <li class="benefit" style="top:591px"><svg class="benefit-icon" viewBox="0 0 42 42"><circle cx="21" cy="21" r="20" fill="var(--lime)" stroke="var(--white)" stroke-width="2"/><circle cx="21" cy="17" r="6" fill="var(--navy)"/><path d="M10 28 H32 M12 32 H30" stroke="var(--navy)" stroke-width="2.5"/></svg><span class="benefit-text">UV fade resistant</span></li>
    <li class="benefit" style="top:643px"><svg class="benefit-icon" viewBox="0 0 42 42"><circle cx="21" cy="21" r="20" fill="var(--lime)" stroke="var(--white)" stroke-width="2"/><path d="M12 22 l6 6 l12 -13" fill="none" stroke="var(--navy)" stroke-width="3.5"/></svg><span class="benefit-text">Won’t bleed, run, or stain once absorbed<br>into the grass</span></li>
    <li class="benefit" style="top:694px"><svg class="benefit-icon" viewBox="0 0 42 42"><circle cx="21" cy="21" r="20" fill="var(--lime)" stroke="var(--white)" stroke-width="2"/><path d="M21 10 L30 13 V21 C30 27 26 30 21 32 C16 30 12 27 12 21 V13 Z" fill="none" stroke="var(--navy)" stroke-width="2.5"/><path d="M17 21 l3 3 l5 -6" fill="none" stroke="var(--navy)" stroke-width="2.5"/></svg><span class="benefit-text">Safe for the environment, pets and people</span></li>
    <li class="benefit" style="top:735px"><svg class="benefit-icon" viewBox="0 0 42 42"><circle cx="21" cy="21" r="20" fill="var(--lime)" stroke="var(--white)" stroke-width="2"/><path d="M21 10 V32 M11 21 H31 M14 14 L28 28 M28 14 L14 28" stroke="var(--navy)" stroke-width="2.5"/></svg><span class="benefit-text">Works in extreme heat, cold and frost</span></li>
    <li class="benefit" style="top:777px"><svg class="benefit-icon" viewBox="0 0 42 42"><circle cx="21" cy="21" r="20" fill="var(--lime)" stroke="var(--white)" stroke-width="2"/><path d="M21 32 V20 M21 22 C14 22 11 17 11 12 C17 12 21 15 21 22 Z M21 22 C28 22 31 17 31 12 C25 12 21 15 21 22 Z" fill="var(--navy)" stroke="var(--navy)" stroke-width="2"/></svg><span class="benefit-text">Organic and natural – no harmful chemicals</span></li>
    <li class="benefit" style="top:830px"><svg class="benefit-icon" viewBox="0 0 42 42"><circle cx="21" cy="21" r="20" fill="var(--lime)" stroke="var(--white)" stroke-width="2"/><circle cx="21" cy="21" r="10" fill="none" stroke="var(--navy)" stroke-width="3"/><path d="M16 21 H26" stroke="var(--navy)" stroke-width="3"/></svg><span class="benefit-text">Reduces the amount of fertilizer<br>and water used on lawns</span></li>
    <li class="benefit" style="top:892px"><svg class="benefit-icon" viewBox="0 0 42 42"><circle cx="21" cy="21" r="20" fill="var(--white)" stroke="var(--lime)" stroke-width="2"/><text x="21" y="29" text-anchor="middle" font-family="Lato, sans-serif" font-weight="900" font-size="22" fill="var(--navy)">$</text></svg><span class="benefit-text">Kerb appeal is essential for getting your<br>property sold for the highest price possible</span></li>
  </ul>

  <div class="compare">
    <div class="compare-half compare-before" role="img" aria-label="Before photo of a dry, patchy backyard lawn"></div>
    <div class="compare-half compare-after" role="img" aria-label="After photo of the same backyard with a green lawn"></div>
    <span class="compare-label" style="top:18px">BEFORE</span>
    <span class="compare-label" style="top:146px">AFTER</span>
  </div>

  <ul class="highlights">
    <li>Instantly restores the natural green colour<br>of grass – year round</li>
    <li>Lasts for up to 3 months</li>
  </ul>

  <div class="contact">900 123 456<br>www.velmoraturf.com</div>

  <ul class="socials">
    <li><span class="dot"></span>Chatterloop</li>
    <li><span class="dot"></span>Snapvista</li>
  </ul>

  <div class="locations">
    <svg width="22" height="26" viewBox="0 0 22 26" aria-hidden="true"><path d="M9 2 a7 7 0 0 1 7 7 C16 14 9 21 9 21 C9 21 2 14 2 9 a7 7 0 0 1 7 -7 Z" fill="var(--lime-bright)"/><circle cx="9" cy="9" r="3" fill="var(--navy)"/><path d="M13 22 H20" stroke="var(--lime-bright)" stroke-width="2.5"/></svg>
    <div class="locations-title">LOCATIONS</div>
    <div class="locations-area">Nowra<br>to Sydney</div>
  </div>
</main>
</body>
</html>
```